Recruiting ad for Caregivers and Nurses

We need a few amazing, fun, catchy, creative recruiting ads for Caregivers and Nurses to care for homecare patients on the island of Oahu, in Hawaii. We are an in home care company called Brantley Homecare. Our care services are provided 24/7, so we need staff that can work days, nights, weekdays, weekends. We need catchy fun ads to entice caregivers and nurses to call our office to inquire about jobs available. Our patients age range is from babies to seniors. We need caregivers and nurses for basic patient care (bathing, dressing, ambulating, preparing meals, medication reminders, light housekeeping) and complex patients (oxygen, tube feeding, injections, vents, wound care). Here are some bullets to consider including:
*Full-time and Part-time Positions Available (days, nights, weekdays, weekends)
*Sign-On Bonus Programs Offered up to $500
*Refer a Friend Bonus Program
*Holiday Pay
*2 Health Plans to Choose from
*Island-Wide Locations
*All PPE Provided (masks, gloves, etc)
*401K Program
*Tuition Benefits

```html
<!DOCTYPE html>
<html lang="en">
<head>
<meta charset="utf-8">
<title>Brantley Homecare – Now Hiring</title>
<link href="https://fonts.googleapis.com/css2?family=Montserrat:wght@400;600;700;800;900&display=swap" rel="stylesheet">
<style>
  :root{
    --green:#1e7a65;
    --green-dark:#145a4a;
    --green-deep:#0f4a3c;
    --mint:#bfe6d8;
    --ink:#1c1c1c;
    --paper:#ffffff;
    --stage:#ececec;
    --peach:#f3a48a;
    --photo-a:#e9e7e3;
    --photo-b:#c9c3bb;
  }
  *{box-sizing:border-box;margin:0;padding:0}
  html,body{width:833px;height:1200px;overflow:hidden}
  body{background:var(--stage);font-family:'Montserrat',sans-serif;color:var(--paper)}
  .poster{position:absolute;left:63px;top:30px;width:707px;height:1140px;background:var(--green);overflow:hidden}
  .hero{position:absolute;left:0;top:0;width:707px;height:515px;background:linear-gradient(90deg,var(--photo-b) 0%,var(--photo-a) 45%,#f2f1ef 100%)}
  .hero-photo{position:absolute;left:0;top:0;width:100%;height:100%}
  .hero-accent{position:absolute;left:305px;top:120px;width:14px;height:170px;background:var(--green)}
  .headline{position:absolute;left:340px;top:118px;font-weight:800;font-size:60px;line-height:1.02;color:var(--ink);letter-spacing:1px}
  .headline-rule{position:absolute;left:340px;top:322px;width:300px;height:12px;background:var(--green)}
  .apply{position:absolute;left:0;top:560px;width:100%;display:flex;justify-content:center;align-items:center;gap:22px}
  .apply h2{font-weight:800;font-size:50px;letter-spacing:1px}
  .positions{position:absolute;top:643px;width:100%;text-align:center;font-size:24px;font-weight:400}
  .positions b{font-weight:800}
  .shifts{position:absolute;top:690px;width:100%;display:flex;justify-content:center;gap:52px;font-size:17px}
  .shifts span{display:flex;align-items:center;gap:10px}
  .dot{width:16px;height:16px;border-radius:50%;background:var(--peach);display:inline-block}
  .divider{position:absolute;left:50px;right:50px;top:737px;height:2px;background:var(--mint);opacity:.6}
  .refer{position:absolute;left:50px;top:768px;display:flex;align-items:center;gap:16px;font-size:15px;line-height:1.35}
  .refer-icon{width:40px;height:32px;border:2px solid var(--paper);border-radius:4px;display:flex;align-items:center;justify-content:center;font-weight:800;font-size:14px}
  .signon{position:absolute;left:300px;top:772px;width:330px;height:34px;background:var(--green-deep);display:flex;align-items:center;padding-left:22px;font-size:13px;font-weight:700}
  .signon em{font-style:normal;color:var(--peach);margin:0 5px}
  .bonus{position:absolute;left:600px;top:757px;width:64px;height:64px;border-radius:50%;background:var(--paper);color:var(--green);display:flex;align-items:center;justify-content:center;font-weight:800;font-size:19px}
  .perks{position:absolute;left:50px;top:880px;list-style:none;font-size:15px;line-height:1.45}
  .perks li{display:flex;gap:12px;margin-bottom:10px}
  .perks li.tight{margin-bottom:0}
  .perks svg{flex:none;margin-top:2px}
  .k401{position:absolute;left:380px;top:910px;width:100px;height:100px;border-radius:50%;background:var(--paper);color:var(--green-dark);display:flex;flex-direction:column;align-items:center;justify-content:center;font-weight:800;font-size:22px;line-height:1.05}
  .k401 small{font-size:12px;font-weight:600}
  .nurse{position:absolute;left:437px;top:850px;width:270px;height:290px;background:linear-gradient(135deg,#ffffff 0%,#eef1f0 60%,#d9e3e0 100%)}
  .brand{position:absolute;left:462px;top:940px;color:var(--green);font-weight:800;font-size:24px;display:flex;align-items:center;gap:8px}
  .brand i{width:14px;height:14px;background:var(--peach);display:inline-block}
  .web{position:absolute;left:50px;top:1090px;font-size:16px;font-weight:600}
</style>
</head>
<body>
<main class="poster">
  <section class="hero">
    <div class="hero-photo" role="img" aria-label="Photo of a toddler sitting on the floor holding a small toy"></div>
    <div class="hero-accent"></div>
    <h1 class="headline">JOANA<br>NEEDS A<br>DOCTOR.</h1>
    <div class="headline-rule"></div>
  </section>

  <div class="apply">
    <svg width="70" height="56" viewBox="0 0 70 56" aria-hidden="true"><path d="M35 52 C10 34 4 24 4 15 A12 12 0 0 1 35 10 A12 12 0 0 1 66 15 C66 24 60 34 35 52Z" fill="none" stroke="var(--mint)" stroke-width="5"/></svg>
    <h2>APPLY TODAY.</h2>
  </div>
  <p class="positions"><b>FULL-TIME</b> and <b>PART-TIME</b> Positions Available</p>
  <div class="shifts">
    <span><i class="dot"></i>days</span>
    <span><i class="dot"></i>nights</span>
    <span><i class="dot"></i>weekdays</span>
    <span><i class="dot"></i>weekends</span>
  </div>
  <div class="divider"></div>

  <div class="refer">
    <div class="refer-icon">+1</div>
    <p>Refer a Friend<br>BONUS Program</p>
  </div>
  <div class="signon">SIGN-ON <em>BONUS</em> Programs offered up to</div>
  <div class="bonus">$500</div>

  <ul class="perks">
    <li class="tight"><svg width="16" height="16" viewBox="0 0 16 16"><circle cx="8" cy="8" r="7" fill="none" stroke="#fff" stroke-width="1.5"/><path d="M4.5 8.2 7 10.5 11.5 5.5" fill="none" stroke="#fff" stroke-width="1.6"/></svg>Holiday Pay</li>
    <li class="tight"><svg width="16" height="16" viewBox="0 0 16 16"><circle cx="8" cy="8" r="7" fill="none" stroke="#fff" stroke-width="1.5"/><path d="M4.5 8.2 7 10.5 11.5 5.5" fill="none" stroke="#fff" stroke-width="1.6"/></svg>2 Health Plans to Choose from</li>
    <li><svg width="16" height="16" viewBox="0 0 16 16"><circle cx="8" cy="8" r="7" fill="none" stroke="#fff" stroke-width="1.5"/><path d="M4.5 8.2 7 10.5 11.5 5.5" fill="none" stroke="#fff" stroke-width="1.6"/></svg>Island-Wide Locations</li>
    <li class="tight"><svg width="16" height="16" viewBox="0 0 16 16"><circle cx="8" cy="8" r="7" fill="none" stroke="#fff" stroke-width="1.5"/><path d="M4.5 8.2 7 10.5 11.5 5.5" fill="none" stroke="#fff" stroke-width="1.6"/></svg>All PPE Provided (masks, gloves, etc)</li>
    <li><svg width="16" height="16" viewBox="0 0 16 16"><circle cx="8" cy="8" r="7" fill="none" stroke="#fff" stroke-width="1.5"/><path d="M4.5 8.2 7 10.5 11.5 5.5" fill="none" stroke="#fff" stroke-width="1.6"/></svg>Tuition Benefits</li>
  </ul>

  <div class="nurse" role="img" aria-label="Photo of a smiling nurse holding a clipboard"></div>
  <div class="brand"><i></i>Brantley</div>
  <div class="k401">401K<small>Program</small></div>

  <p class="web">brantleycare.com</p>
</main>
</body>
</html>
```